Course Lantern

CourseLantern.example will be a place for people looking for information, resources, and advisement to start or continue their education. We want a friendly, inviting site design that makes finding what potential students are looking for simple and easy to navigate. We are not committed to the colors of the logo, so variations on the color scheme are welcome.

Text instructions based on the wireframe: For the site's homepage we'd like a banner at the very top for our Logo and white space to the right of it. See attachments for logo + wireframe. Below that would be navigation. Below that split into 2/3 on the left we would have home page content, and 1/3 on the right we would have the lead form. At the bottom of the page we would have a space for types of degrees, then a footer with copyright info + site info.

See wireframes for additional page layouts.

Industry/Entity Type

Education

Requirements
Must have
• At minimum we are looking for three pages: homepage, choose your degree path page, and content page.
Nice to have
• -White space is appreciated
-Variations on the color scheme are welcome, we are not married to the existing logo's color scheme.

```html
<!DOCTYPE html>
<html lang="en">
<head>
<meta charset="utf-8">
<title>Course Lantern — Home</title>
<link href="https://fonts.googleapis.com/css2?family=Arimo:wght@400;700&family=Oswald:wght@600&display=swap" rel="stylesheet">
<style>
:root{
  --green:#7aab2a;
  --green-dark:#5b8a1a;
  --green-light:#a6cf3c;
  --orange:#f26a1b;
  --orange-btn:#f39a1a;
  --ink:#2b3a42;
  --text:#444;
  --grey-bg:#ececec;
  --panel:#f3f3f3;
  --dark:#4a4a4a;
  --footer:#e0e0e0;
}
*{box-sizing:border-box;margin:0;padding:0}
html,body{width:1200px;height:1151px;overflow:hidden}
body{position:relative;background:linear-gradient(#f2f2f2,#f7f7f7 60%,#e9e9e9);font-family:Arimo,Arial,sans-serif;color:var(--text)}
.abs{position:absolute}
.header{left:150px;top:0;width:900px;height:153px;background:linear-gradient(#f6f6f6,#fff);border-left:1px solid #ddd;border-right:1px solid #ddd}
.account-tab{left:697px;top:0;width:106px;height:25px;background:var(--green);border-radius:0 0 6px 6px;color:#fff;font-size:12px;display:flex;align-items:center;justify-content:center;gap:8px}
.account-tab span:first-child{color:#e6f3cc}
.logo{left:166px;top:78px;display:flex;align-items:center;gap:10px}
.logo-mark{width:26px;height:26px;background:var(--orange)}
.logo-name{font-size:42px;font-weight:700;color:var(--ink);letter-spacing:-1px}
.call{left:580px;top:124px;font-size:16px;color:#aaa}
.call b{color:var(--green);font-size:20px}
.students-photo{left:825px;top:6px;width:215px;height:147px;background:linear-gradient(135deg,#d8d0c8,#6b6b6b 55%,#9cc93a);border-radius:4px}
.nav{left:139px;top:153px;width:922px;height:48px;background:linear-gradient(var(--green-light),var(--green));box-shadow:0 2px 2px rgba(0,0,0,.2)}
.nav ul{list-style:none;display:flex;position:absolute;left:11px;top:6px;gap:0}
.nav li{color:#fff;font-size:14px;font-weight:700;padding:9px 15px;height:35px;border-radius:5px}
.nav li.active{background:var(--orange)}
.search{left:755px;top:157px;width:288px;height:40px;background:#fff;border:1px solid #d8d8d8;border-radius:3px}
.search span{position:absolute;left:9px;top:13px;font-size:12px;font-style:italic;color:#999}
.search b{position:absolute;right:2px;top:2px;width:42px;height:34px;background:linear-gradient(#f7b32a,#ee8a10);color:#fff;font-size:18px;border-radius:3px;display:flex;align-items:center;justify-content:center}
.welcome{left:150px;top:201px;width:900px;height:146px;background:var(--panel);border:1px solid #ddd;border-top:0;border-radius:0 0 8px 8px}
.welcome .divider{left:398px;top:10px;width:1px;height:122px;background:#ccc}
.arrow{width:38px;height:38px;border-radius:50%}
.welcome-kicker{left:58px;top:32px;font-size:24px;color:var(--orange)}
.welcome-title{left:58px;top:64px;width:332px;font-size:27px;font-weight:700;color:var(--ink);white-space:nowrap;letter-spacing:-.3px}
.invest{left:433px;top:12px;width:420px}
.invest h2{font-size:23px;font-weight:400;color:var(--orange)}
.invest h3{font-size:13px;font-weight:400;color:var(--green);margin-top:9px}
.invest p{font-size:11px;line-height:17px;color:#555;margin-top:8px}
.invest em{display:block;font-size:13.5px;color:#222;margin-top:12px}
.about{left:170px;top:384px;width:553px}
.about h1{font-size:24px;font-weight:400;color:var(--green);padding-bottom:24px;border-bottom:1px dotted #999}
.about p{font-size:11.5px;line-height:22.5px;text-indent:34px;margin-top:19px;text-align:justify;color:#333}
.about p+p{margin-top:22px}
.read-more{height:26px;width:104px;border-radius:13px;background:linear-gradient(#fff,#ddd);border:1px solid #ccc;box-shadow:0 1px 2px rgba(0,0,0,.2);font-size:12px;color:#444;display:flex;align-items:center;padding-left:13px;gap:7px;white-space:nowrap}
.read-more i{width:16px;height:16px;border-radius:50%;background:var(--green);display:inline-flex;align-items:center;justify-content:center;flex:none}
.lead-form{left:755px;top:368px;width:290px;height:446px;background:linear-gradient(160deg,#a2cc3c,#6fa126 60%,#5a8c1c);border:2px solid #b6da5a;border-radius:8px;color:#fff}
.lead-form h2{position:absolute;left:8px;top:6px;font-family:Oswald,Arial,sans-serif;font-size:28px;font-weight:600;letter-spacing:-.3px}
.lead-form .intro{position:absolute;left:10px;top:46px;width:270px;font-size:11.5px;line-height:17px}
.lead-form .match{position:absolute;left:9px;top:86px;font-size:13.5px;color:#ffef3a}
.lead-form .req{position:absolute;left:98px;top:113px;font-size:8px;letter-spacing:1.5px;color:#e8f56a}
.field{position:absolute;left:10px;width:280px;height:20px;font-size:11px}
.field label{position:absolute;left:0;top:3px;line-height:13px}
.field .box{position:absolute;left:90px;top:0;width:177px;height:21px;background:#f8f8f3;border:1px solid #c9d6a8;border-radius:2px}
.field .drop::after{content:"";position:absolute;right:4px;top:3px;width:14px;height:13px;background:#ccc;border-radius:2px;clip-path:polygon(0 0,100% 0,50% 100%)}
.btn-request{left:98px;top:399px;width:179px;height:36px;background:linear-gradient(#fbc02d,#ef8a10);border:1px solid #fce07a;border-radius:5px;font-family:Oswald,Arial,sans-serif;font-size:19px;color:#8a3b06;display:flex;align-items:center;justify-content:center}
.privacy{left:770px;top:825px;width:256px;text-align:center;font-size:11px;line-height:13px;color:#222}
.footer{left:0;top:862px;width:1200px;height:289px;background:linear-gradient(#e6e6e6,#d8d8d8);border-top:3px solid #555}
.content-box{left:144px;top:845px;width:242px;height:242px;background:var(--dark);border-radius:0 0 6px 6px;color:#ddd}
.content-box h3{position:absolute;left:13px;top:41px;font-size:14px;color:var(--green-light)}
.content-box p{position:absolute;left:13px;top:71px;width:215px;font-size:11.5px;line-height:17px;color:#e0e0e0;text-align:justify}
.types-title{left:418px;top:884px;font-size:14px;font-weight:700;color:var(--green)}
.degree-list{list-style:none;width:178px}
.degree-list li{height:34px;border-bottom:1px dotted #aaa;font-size:12px;color:#222;display:flex;align-items:center;gap:19px;padding-left:4px}
.degree-list li.active{background:var(--orange);color:#fff;border-bottom-color:transparent}
.bullet{width:14px;height:14px;border-radius:50%;background:#eee;border:1px solid #bbb;display:inline-flex;align-items:center;justify-content:center}
.copyright{left:413px;top:1075px;width:520px;white-space:nowrap;font-size:10.5px;letter-spacing:.3px;color:#444}
.copyright span{color:var(--green)}
.social{top:1065px;width:31px;height:31px;border-radius:50%;background:linear-gradient(#fff,#ddd);border:1px solid #ccc}
</style>
</head>
<body>
<header class="abs header"></header>
<div class="abs account-tab"><span>Login</span><span>|</span><span>Register</span></div>
<div class="abs logo"><span class="logo-mark"></span><span class="logo-name">Course Lantern</span></div>
<div class="abs call">Call Us: <b>800-555-0199</b></div>
<div class="abs students-photo" role="img" aria-label="Photo of four smiling students holding notebooks"></div>

<nav class="abs nav">
  <ul>
    <li class="active">Home</li><li>About Us</li><li>Feedback</li><li>Privacy Policy</li><li>Terms of Use</li><li>Contact Us</li>
  </ul>
</nav>
<div class="abs search"><span>Type text here</span><b>Go</b></div>

<section class="abs welcome">
  <svg class="abs arrow" style="left:6px;top:63px" viewBox="0 0 38 38"><circle cx="19" cy="19" r="18" fill="#f4f4f4" stroke="#bbb"/><path d="M23 11 13 19 23 27z" fill="#888"/></svg>
  <div class="abs welcome-kicker">WELCOME TO</div>
  <div class="abs welcome-title">CourseLantern.example</div>
  <div class="abs divider"></div>
  <div class="abs invest">
    <h2>Invest In Your Future Today</h2>
    <h3>Are you overwhelmed by the thought of choosing the right college?</h3>
    <p>CourseLantern helps simplify this process by matching colleges to you<br>and your needs. Tell us about yourself and let us do the work for you.</p>
    <em>Take control of your future by furtheing your education.</em>
  </div>
  <svg class="abs arrow" style="left:857px;top:63px" viewBox="0 0 38 38"><circle cx="19" cy="19" r="18" fill="#6fa126" stroke="#4d7a14"/><path d="M15 11 26 19 15 27z" fill="#fff"/></svg>
</section>

<main class="abs about">
  <h1>About Course Lantern</h1>
  <p>CourseLantern.example is a free resource to start your path to a college degree and compare higher education options that can generally lead to improved career or job opportunities based on numerous employment reports from organizations like the National Jobs Bureau. Our free education tools and resources do not guarantee employment nor an offer of employment.</p>
  <p>Our mission is to match you with the top colleges, universities or technical institutions that offer the higher education programs that meet your goals, based on the information you provided. Enrollment and Education Experts at the Private &amp; Public Institutions we partner with can provide you with additional, detailed information on a) applying for their school b) tuition costs and tuition assistance for their school and c) career and employment information and statistics for students that have successfully completed programs in that field or from their particular school.</p>
</main>
<div class="abs read-more" style="left:613px;top:717px">Read more <i><svg width="10" height="10" viewBox="0 0 10 10"><path d="M1 5h7M5 2l3 3-3 3" stroke="#fff" stroke-width="1.6" fill="none"/></svg></i></div>

<aside class="abs lead-form">
  <h2>Tell us more about YOU!</h2>
  <p class="intro">CourseLantern provides you with accredite school information that match your interests.</p>
  <p class="match">Get matched to the right schools today.</p>
  <span class="req">*Required fields</span>
  <div class="field" style="top:131px"><label>Subject*</label><span class="box drop"></span></div>
  <div class="field" style="top:159px"><label>Degree Level*</label><span class="box drop"></span></div>
  <div class="field" style="top:187px"><label>High School<br>Grad Yr.*</label><span class="box drop"></span></div>
  <div class="field" style="top:229px"><label>First Name*</label><span class="box"></span></div>
  <div class="field" style="top:257px"><label>Last Name*</label><span class="box"></span></div>
  <div class="field" style="top:285px"><label>Street Address*</label><span class="box"></span></div>
  <div class="field" style="top:313px"><label>Zip / City / State*</label>
    <span class="box" style="width:52px"></span><span class="box" style="left:145px;width:65px"></span><span class="box" style="left:213px;width:54px"></span></div>
  <div class="field" style="top:341px"><label>Phone Number*</label><span class="box"></span></div>
  <div class="field" style="top:369px"><label>Email Address*</label><span class="box"></span></div>
  <div class="abs btn-request">Request Information</div>
</aside>
<p class="abs privacy">Your information will be kept strictly private as stated in our Privacy Policy.</p>

<footer class="abs footer"></footer>
<div class="abs content-box">
  <h3>Degree Content?</h3>
  <p>Duis autem vel eum iriure dolor in hendrerit in vulputate velit esse molestie consequat, vel illum dolore eu feugiat nulla facilisis at vero eros et accumsan et iusto odio dignissim qui blandit praesent luptatum zzril delenit.</p>
  <div class="abs read-more" style="left:123px;top:198px">Read more <i><svg width="10" height="10" viewBox="0 0 10 10"><path d="M1 5h7M5 2l3 3-3 3" stroke="#fff" stroke-width="1.6" fill="none"/></svg></i></div>
</div>

<h3 class="abs types-title">Types of Degree</h3>
<ul class="abs degree-list" style="left:420px;top:908px">
  <li><span class="bullet"></span>Degree Type One here</li>
  <li class="active"><span class="bullet"></span>Degree Type Two here</li>
  <li><span class="bullet"></span>Degree Type Three here</li>
  <li><span class="bullet"></span>Degree Type Four here</li>
</ul>
<ul class="abs degree-list" style="left:645px;top:908px">
  <li><span class="bullet"></span>Degree Type Five here</li>
  <li><span class="bullet"></span>Degree Type Six here</li>
  <li><span class="bullet"></span>Degree Type Seven here</li>
  <li><span class="bullet"></span>Degree Type Eight here</li>
</ul>
<ul class="abs degree-list" style="left:869px;top:908px">
  <li><span class="bullet"></span>Degree Type Nine here</li>
  <li><span class="bullet"></span>Degree Type Ten here</li>
  <li><span class="bullet"></span>Degree Type Elevent here</li>
  <li><span class="bullet"></span>Degree Type One here</li>
</ul>

<p class="abs copyright">© Copyright 2009-2012 <span>CourseLantern.example</span>™ &amp; Brightpath, Inc. All Rights Reserved.</p>
<span class="abs social" style="left:949px"></span>
<span class="abs social" style="left:984px"></span>
<span class="abs social" style="left:1019px"></span>
</body>
</html>
```